KVRo Business Cards

We need a business card design. We are a Technology (Audio Visual) design, sales and installation company. Looking for a double sided design, clean

Contact Information for Business Card

Clean, modern look, 2 sided

Font styles to use
Sans Serif

```html
<!DOCTYPE html>
<html lang="en">
<head>
<meta charset="utf-8">
<title>KVRo Business Cards</title>
<link href="https://fonts.googleapis.com/css2?family=Raleway:wght@500;800&family=Source+Sans+3:wght@300;400&display=swap" rel="stylesheet">
<style>
  :root {
    --navy: #1b2f3e;
    --orange: #f7941d;
    --white: #ffffff;
    --ink-soft: #4a4f55;
    --rule: #5b6168;
    --backdrop: #e9e7e4;
  }
  * { box-sizing: border-box; margin: 0; padding: 0; }
  html, body {
    width: 1125px;
    height: 1200px;
    overflow: hidden;
    background: var(--backdrop);
  }
  .stage {
    position: absolute;
    left: 150px;
    top: 90px;
    width: 800px;
    transform: scale(1.03);
    transform-origin: 0 0;
  }
  .card {
    position: relative;
    width: 800px;
    height: 455px;
    overflow: hidden;
    box-shadow: 0 3px 10px rgba(0,0,0,0.18);
  }
  .card + .card { margin-top: 62px; }
  .card--front { background: var(--white); }
  .card--back { background: var(--navy); }

  .wordmark {
    font-family: "Raleway", sans-serif;
    font-weight: 800;
    letter-spacing: 2px;
    line-height: 1;
    position: absolute;
  }
  .card--front .wordmark {
    color: var(--navy);
    font-size: 150px;
    right: 50px;
    top: 36px;
  }
  .card--back .wordmark {
    color: var(--white);
    font-size: 200px;
    left: 0;
    right: 0;
    top: 128px;
    text-align: center;
  }

  .holder {
    position: absolute;
    left: 48px;
    top: 276px;
  }
  .holder__name {
    font-family: "Raleway", sans-serif;
    font-weight: 500;
    font-size: 26px;
    color: var(--navy);
    letter-spacing: 0.3px;
  }
  .holder__title {
    font-family: "Raleway", sans-serif;
    font-weight: 500;
    font-size: 17px;
    color: var(--orange);
    margin-top: 2px;
  }
  .divider {
    position: absolute;
    left: 48px;
    right: 51px;
    top: 342px;
    height: 1px;
    background: var(--rule);
  }
  .contact {
    position: absolute;
    top: 360px;
    font-family: "Source Sans 3", sans-serif;
    font-weight: 300;
    font-size: 17.5px;
    line-height: 23px;
    color: var(--ink-soft);
    letter-spacing: 0.4px;
  }
  .contact--left { left: 48px; }
  .contact--right { right: 51px; text-align: right; }
  .contact__sep { margin: 0 4px; }

  .edge-band {
    position: absolute;
    left: 0;
    bottom: 0;
    width: 800px;
    height: 10px;
    display: block;
  }
</style>
</head>
<body>
  <main class="stage">
    <section class="card card--front" aria-label="Business card front">
      <div class="wordmark">KVRo</div>

      <div class="holder">
        <div class="holder__name">DANIEL REYES</div>
        <div class="holder__title">President</div>
      </div>

      <div class="divider"></div>

      <address class="contact contact--left" style="font-style:normal">
        412-730-5586<br>
        info@kvro.com<span class="contact__sep">|</span>www.kvro.com
      </address>
      <address class="contact contact--right" style="font-style:normal">
        1420 Cedar Hollow Road<br>
        Juneau, Alaska 99801
      </address>

      <svg class="edge-band" viewBox="0 0 800 10" aria-hidden="true">
        <polygon points="0,0 523,0 520,10 0,10" fill="var(--navy)"/>
        <polygon points="528,0 800,0 800,10 525,10" fill="var(--orange)"/>
      </svg>
    </section>

    <section class="card card--back" aria-label="Business card back">
      <div class="wordmark">KVRo</div>
    </section>
  </main>
</body>
</html>
```